Lumen Business Cards

We need a new look business cvard to refelect our new look website www.lumenplan.com.au
We’re Lumen, a team of town planning and traffic and transport engineering specialists located in Melbourne.

Lumen is a company that is structured, articulate, dynamic, progressive, accurate and adaptable.
Our key messages are:
1. We make your life easier by doing what we do best
2. We tell you what you need to know not what you want to hear
3. Polished and professional but not afraid to show some personality

we would like a bold new look that is polished and professional but not afraid to show a bit of personality

Target Market(s)

Lumen’s diverse client base consists of architecture practices, builders, developers, local government and the legal fraternity.

Industry/Entity Type

Town

Requirements
Must have
• must use our logo and have the following information

Joel Petrakis
Director

Lumen Advisory Pty Ltd
Hillgate first floor
Cotter Street
Kewdale VIC 3187 Australia
+61 03 9581 6724
mail@lumenplan.com.au
www.lumenplan.com.au
Nice to have
• We would like to see the logo used or the colours of the logo used.

```html
<!DOCTYPE html>
<html lang="en">
<head>
<meta charset="utf-8">
<title>Lumen Business Cards</title>
<link href="https://fonts.googleapis.com/css2?family=Source+Sans+3:wght@400;600;700&display=swap" rel="stylesheet">
<style>
  :root {
    --backdrop: #ece9e4;
    --card: #ffffff;
    --card-shade: #f1f1f1;
    --band: #6d6e71;
    --band-light: #8a8b8e;
    --ink: #2b2b2b;
    --ink-soft: #4a4a4a;
    --on-band: #ffffff;
    --field: #f4f4f4;
    --blue: #1aa3e8;
    --sky: #a9d8f2;
    --mint: #8fd0a8;
    --green: #0e8a3e;
    --deep-green: #0b6b30;
  }
  * { box-sizing: border-box; margin: 0; padding: 0; }
  html, body {
    width: 1200px; height: 800px; overflow: hidden;
    background: var(--backdrop);
    font-family: "Source Sans 3", sans-serif;
  }
  .sheet {
    width: 1200px; height: 800px;
    display: flex; align-items: center; justify-content: center; gap: 60px;
  }
  .card {
    position: relative; width: 500px; height: 290px; overflow: hidden;
    background: radial-gradient(circle at 60% 45%, var(--card) 0%, var(--card-shade) 100%);
    box-shadow: 0 6px 18px rgba(0,0,0,.22);
  }
  .card-band { position: absolute; inset: 0; width: 100%; height: 100%; }

  /* front */
  .holder { position: absolute; left: 28px; top: 52px; color: var(--ink); }
  .holder-name { font-weight: 700; font-size: 22px; line-height: 1.1; }
  .holder-role { font-weight: 400; font-size: 20px; line-height: 1.15; color: var(--ink-soft); }
  .brand-lockup {
    position: absolute; right: 48px; top: 112px;
    display: flex; align-items: center; gap: 10px;
  }
  .brand-name { font-size: 34px; font-weight: 400; color: var(--band); letter-spacing: .5px; }
  .brand-square { width: 26px; height: 26px; background: var(--green); }
  .address {
    position: absolute; left: 24px; top: 190px;
    color: var(--on-band); font-size: 12.5px; line-height: 1.3;
  }
  .address-company { font-weight: 700; }
  .contact {
    position: absolute; right: 22px; top: 218px;
    color: var(--on-band); font-size: 12.5px; line-height: 1.3; text-align: right;
  }
  .contact b { font-weight: 700; }

  /* back */
  .dot-field {
    position: absolute; left: 300px; top: 0; width: 200px; height: 290px;
    background: var(--field);
  }
  .wordmark-band {
    position: absolute; left: 0; top: 48px; width: 420px; height: 124px;
    background: linear-gradient(90deg, var(--band) 0%, var(--band-light) 60%, var(--band) 100%);
    display: flex; align-items: center; justify-content: center;
  }
  .wordmark {
    color: var(--on-band); font-size: 118px; font-weight: 400;
    line-height: 1; letter-spacing: 2px; margin-top: -10px;
  }
  .colour-run {
    position: absolute; left: 0; top: 196px; width: 460px; height: 58px;
    background: linear-gradient(90deg, var(--blue) 0%, var(--sky) 35%, var(--mint) 55%, var(--green) 85%, var(--deep-green) 100%);
  }
</style>
</head>
<body>
<main class="sheet">

  <section class="card card-front" aria-label="Business card front">
    <svg class="card-band" viewBox="0 0 500 290" preserveAspectRatio="none" aria-hidden="true">
      <polygon points="0,168 500,178 500,290 0,268" fill="var(--band)"/>
    </svg>
    <div class="holder">
      <p class="holder-name">Joel Petrakis</p>
      <p class="holder-role">Director</p>
    </div>
    <div class="brand-lockup">
      <span class="brand-name">lumen</span>
      <span class="brand-square"></span>
    </div>
    <address class="address" style="font-style:normal">
      <p class="address-company">Lumen Advisory Pty Ltd</p>
      <p>Hillgate first floor</p>
      <p>Cotter Street</p>
      <p>Kewdale VIC 3187 Australia</p>
    </address>
    <div class="contact">
      <p><b>tel:</b> +61 03 9581 6724</p>
      <p><b>web:</b> www.lumenplan.com.au</p>
      <p><b>email:</b> mail@lumenplan.com.au</p>
    </div>
  </section>

  <section class="card card-back" aria-label="Business card back">
    <div class="dot-field" role="img" aria-label="Light field of fine grey dots"></div>
    <div class="wordmark-band">
      <span class="wordmark">lumen</span>
    </div>
    <div class="colour-run" role="img" aria-label="Stepped run of blue to green tiles"></div>
  </section>

</main>
</body>
</html>
```